Logo + Business Card design for a new start-up

For a new start-up company, a global brand expansion agency (marketing, brand consulting solutions) we're looking for a creative designer to help us design both the company logo and business card for project managers.

The name of the company is 'Harrowgate Market Partners' (abbreviated: HMP, website: harrowgatemarketpartners.example)

The logo design should give the company an image of "corporate" (serious), but not too plain/simple. Playing with overlapping fonts, or font colors is an option. Logo with only the abbreviation HMP is also an option.

The business cards need to have a touch of creativity to them, any style/colors can be used, and should underline the nature of business.

```html
<!DOCTYPE html>
<html lang="en">
<head>
<meta charset="utf-8">
<title>Harrowgate Market Partners – Business Cards</title>
<link rel="stylesheet" href="https://fonts.googleapis.com/css2?family=Open+Sans:ital,wght@0,400;0,600;1,400&display=swap">
<style>
  :root {
    --brand-blue: #1d6fb8;
    --brand-red: #e5222e;
    --card-white: #ffffff;
    --ink: #1b1b1b;
    --backdrop: #e9e6e1;
  }
  * { margin: 0; padding: 0; box-sizing: border-box; }
  html, body { width: 1200px; height: 891px; overflow: hidden; }
  body {
    background: var(--backdrop);
    font-family: "Open Sans", Arial, sans-serif;
    display: flex;
    align-items: center;
    justify-content: center;
    gap: 60px;
  }
  .card {
    position: relative;
    width: 530px;
    height: 310px;
    background: var(--card-white);
    box-shadow: 0 6px 20px rgba(0,0,0,0.15);
    overflow: hidden;
  }
  .edge-tab {
    position: absolute;
    width: 16px;
    height: 80px;
    border-radius: 8px;
  }
  .edge-tab--blue { background: var(--brand-blue); left: -8px; }
  .edge-tab--red { background: var(--brand-red); right: -8px; }

  .card--front .edge-tab--blue { top: 78px; }
  .card--front .edge-tab--red { top: 168px; }

  .card--contact .edge-tab--blue { top: 18px; }
  .card--contact .edge-tab--red { bottom: 18px; }

  .wordmark {
    position: absolute;
    display: flex;
    align-items: center;
    gap: 14px;
    color: var(--brand-blue);
    font-weight: 600;
    white-space: nowrap;
  }
  .wordmark__mark {
    width: 20px;
    height: 20px;
    background: var(--brand-red);
    flex: none;
  }
  .card--front .wordmark {
    left: 62px;
    top: 128px;
    font-size: 29px;
  }
  .card--contact .wordmark {
    left: 62px;
    top: 52px;
    font-size: 29px;
  }
  .contact {
    position: absolute;
    left: 60px;
    width: 270px;
    top: 128px;
    text-align: right;
    color: var(--ink);
    font-size: 13px;
    line-height: 1.55;
  }
  .contact__name { font-weight: 600; font-size: 16px; }
  .contact__role { font-style: italic; margin-bottom: 4px; }
</style>
</head>
<body>
  <section class="card card--front" aria-label="Business card front">
    <span class="edge-tab edge-tab--blue"></span>
    <span class="edge-tab edge-tab--red"></span>
    <div class="wordmark">
      <span class="wordmark__mark"></span>
      <span class="wordmark__name">Harrowgate Market Partners</span>
    </div>
  </section>

  <section class="card card--contact" aria-label="Business card back">
    <span class="edge-tab edge-tab--blue"></span>
    <span class="edge-tab edge-tab--red"></span>
    <div class="wordmark">
      <span class="wordmark__mark"></span>
      <span class="wordmark__name">Harrowgate Market Partners</span>
    </div>
    <div class="contact">
      <p class="contact__name">Daniel Reeve</p>
      <p class="contact__role">Project Manager</p>
      <p>Tel: 000 000 0000</p>
      <p>Fax: 000 000 0000</p>
      <p>E-mail: daniel.reeve@hmp.example</p>
      <p>www.harrowgatemarketpartners.example</p>
    </div>
  </section>
</body>
</html>
```